Harborline 52 Sailing Magazine

I need a magazine layout for a new sailing magazine (called 'Harborline 52'). I would like to see designs for both the cover as well as the inside spread and the template should allow for content to be dropped into it. Please note that on an ongoing basis, I would prefer to provide the content to the designer, who then adds it to the template, making the necessary edits).

Colors

Designer to choose colors to be used in the design.

Requirements
Must have
• Classy modern design, nautical colors and theme (but clean and modern)
Should not have
• Tacky, old school sailing stuff. Also, here is a great example of how I don't want it to look! Like so many other magazines, the ads take over and give the magazine a very unsophisticated feel. Click on the magazine at this website to see it's inside pages:
• https://www.windquaymag.example/

```html
<!DOCTYPE html>
<html lang="en">
<head>
<meta charset="utf-8">
<title>Harborline 52 — Cover and Spread Template</title>
<link rel="stylesheet" href="https://fonts.googleapis.com/css2?family=Oswald:wght@500;700&family=Open+Sans:wght@400;600;700&display=swap">
<style>
  :root{
    --board:#e6e7e9;
    --paper:#ffffff;
    --navy:#0f3f7a;
    --blue:#1c64b4;
    --sky:#3f8fd6;
    --cyan:#2bb3dc;
    --red:#d7263d;
    --ink:#3a3f47;
    --muted:#8a9099;
    --rule:#dfe3e8;
  }
  *{box-sizing:border-box;margin:0;padding:0}
  html,body{width:800px;height:1200px;overflow:hidden;background:var(--board);font-family:"Open Sans",Arial,sans-serif;color:var(--ink)}
  .board{position:relative;width:800px;height:1200px}
  .page{position:absolute;background:var(--paper);box-shadow:0 3px 10px rgba(0,0,0,.18);overflow:hidden}

  /* Cover */
  .cover{left:200px;top:75px;width:288px;height:477px;background:linear-gradient(180deg,var(--blue) 0%,var(--navy) 32%)}
  .cover-masthead{position:absolute;left:16px;top:18px;font-family:"Oswald",sans-serif;font-weight:700;font-size:40px;line-height:1;color:#fff;letter-spacing:.5px}
  .cover-issue{position:absolute;left:16px;top:64px;font-family:"Oswald",sans-serif;font-weight:500;font-size:18px;color:#fff}
  .cover-issue .year{color:var(--red)}
  .cover-tagline{position:absolute;left:16px;top:92px;font-family:"Oswald",sans-serif;font-weight:500;font-size:17px;color:#fff}
  .cover-photo{position:absolute;left:0;top:126px;width:288px;height:282px;background:linear-gradient(180deg,#8fb4d6 0%,#5e89b0 30%,#2f5d86 55%,#1d4a78 100%)}
  .cover-insets{position:absolute;left:0;top:318px;width:288px;display:flex;justify-content:center;gap:10px}
  .cover-inset{width:58px;height:58px;border-radius:50%;border:3px solid #fff;background:linear-gradient(160deg,#b9d7ee,#4a86b8)}
  .cover-footer{position:absolute;left:0;bottom:0;width:288px;height:69px;background:#fff;padding:14px 16px;font-size:7px;line-height:1.5;color:var(--ink)}
  .cover-footer strong{color:var(--navy)}

  /* Back / stationery page */
  .sheet{left:508px;top:80px;width:225px;height:467px}
  .sheet-brand{position:absolute;right:14px;top:14px;font-family:"Oswald",sans-serif;font-weight:700;font-size:9px;color:var(--red)}
  .sheet-lines{position:absolute;left:16px;top:46px;width:193px}
  .sheet-lines span{display:block;height:3px;background:#f1f2f4;margin-bottom:9px}
  .sheet-band{position:absolute;left:0;bottom:0;width:225px;height:60px;background:var(--red);display:flex;align-items:center;justify-content:space-between;padding:0 16px;color:#fff}
  .sheet-band .name{font-family:"Oswald",sans-serif;font-weight:700;font-size:14px}
  .sheet-band .phone{font-family:"Oswald",sans-serif;font-weight:500;font-size:15px}

  /* Spread */
  .spread{left:107px;top:581px;width:626px;height:464px;display:flex}
  .spread-page{position:relative;width:313px;height:464px}
  .spread-left{border-right:1px solid var(--rule)}
  .edge-strip{position:absolute;left:0;top:0;width:10px;height:464px;background:var(--cyan)}
  .feature-title{font-family:"Oswald",sans-serif;font-weight:700;line-height:1}
  .marina-title{position:absolute;left:22px;top:16px;font-size:24px;color:var(--cyan)}
  .marina-sub{position:absolute;left:22px;top:44px;font-size:6.5px;font-weight:700;letter-spacing:.6px;color:var(--ink)}
  .marina-photo{position:absolute;left:22px;top:58px;width:278px;height:112px;background:linear-gradient(180deg,#9cc6e6 0%,#cfe2ef 45%,#3a7ea8 75%,#2a5f86 100%)}
  .caption-bar{position:absolute;left:22px;top:170px;width:150px;height:14px;background:var(--cyan);color:#fff;font-family:"Oswald",sans-serif;font-size:8px;padding:2px 6px}
  .body-copy{font-size:5px;line-height:1.55;color:var(--ink)}
  .section-head{font-size:5.5px;font-weight:700;color:var(--red);letter-spacing:.4px;margin-bottom:3px}
  .marina-copy{position:absolute;left:22px;top:192px;width:278px}
  .marina-copy p{margin-bottom:5px}
  .tick-list{list-style:none;display:grid;grid-template-columns:1fr 1fr;column-gap:12px;row-gap:2px;margin-bottom:6px}
  .tick-list li{font-size:5px;display:flex;gap:4px;align-items:center}
  .tick-list svg{flex:none}
  .marina-contact{position:absolute;left:22px;bottom:16px;width:278px;display:flex;justify-content:space-between;align-items:flex-end}
  .marina-badge{display:flex;align-items:center;gap:5px;font-family:"Oswald",sans-serif;font-weight:500;font-size:9px;color:var(--cyan)}
  .marina-badge i{display:block;width:12px;height:12px;background:var(--cyan)}
  .marina-contact .body-copy{text-align:right}

  .out-title{position:absolute;left:16px;top:16px;width:150px;font-size:18px;color:var(--red)}
  .out-intro{position:absolute;left:16px;top:64px;width:140px}
  .sail-photo{position:absolute;left:166px;top:16px;width:132px;height:120px;background:linear-gradient(180deg,#d9e6ef 0%,#a8c3d8 55%,#5e87a6 100%)}
  .out-col{position:absolute;left:166px;top:142px;width:132px}
  .callout{position:absolute;left:16px;top:160px;width:140px;height:54px;background:var(--red);color:#fff;padding:7px 8px;font-size:5.5px;line-height:1.5}
  .callout b{font-family:"Oswald",sans-serif;font-size:8px;display:block;margin-bottom:2px}
  .out-text2{position:absolute;left:16px;top:220px;width:282px}
  .photo-row{position:absolute;left:16px;top:286px;width:282px;display:flex;gap:6px}
  .photo-row div{flex:1;height:62px}
  .photo-a{background:linear-gradient(180deg,#c7dced,#6f97b8)}
  .photo-b{background:linear-gradient(180deg,#e4eef5,#8fb0c8)}
  .photo-c{background:linear-gradient(180deg,#bcd8c4,#4f8aa8)}
  .ad{position:absolute;left:16px;top:362px;width:282px;height:86px;border-top:1px solid var(--rule);padding-top:10px;display:flex;gap:10px}
  .ad-mark{width:62px;height:62px;background:var(--red);flex:none}
  .ad-info{flex:1}
  .ad-name{font-family:"Oswald",sans-serif;font-weight:700;font-size:15px;color:var(--navy);margin-bottom:6px}
  .ad-line{display:flex;align-items:center;gap:5px;font-size:6px;margin-bottom:3px}
</style>
</head>
<body>
<main class="board">

  <section class="page cover" aria-label="Magazine cover">
    <h1 class="cover-masthead">HARBORLINE 52</h1>
    <p class="cover-issue">VOLUME 510 December <span class="year">2019</span></p>
    <p class="cover-tagline">We Go Where The Wind Blows</p>
    <div class="cover-photo" role="img" aria-label="Photo of a white motor yacht cruising on blue water in front of an island"></div>
    <div class="cover-insets">
      <div class="cover-inset" role="img" aria-label="Inset photo of a sailboat race"></div>
      <div class="cover-inset" role="img" aria-label="Inset photo of colourful sails"></div>
      <div class="cover-inset" role="img" aria-label="Inset photo of a boat heeling in the wind"></div>
    </div>
    <div class="cover-footer">
      <strong>Sign Up For 25% Season Charges Plus A Weekend Getaway</strong><br>
      North Bay Regatta Preview, Harbor News and Crew Tips Inside
    </div>
  </section>

  <section class="page sheet" aria-label="Back page">
    <div class="sheet-brand">Harborline 52</div>
    <div class="sheet-lines"><span></span><span></span><span></span></div>
    <div class="sheet-band">
      <span class="name">Harborline 52</span>
      <span class="phone">0123 555 789</span>
    </div>
  </section>

  <section class="page spread" aria-label="Inside spread">
    <article class="spread-page spread-left">
      <div class="edge-strip"></div>
      <h2 class="feature-title marina-title">BAYFRONT MARINA</h2>
      <p class="marina-sub">MANY THANKS AND WARM HOLIDAY WISHES</p>
      <div class="marina-photo" role="img" aria-label="Photo of boats moored at a marina dock under a blue sky"></div>
      <div class="caption-bar">FROM ALL OF US HERE AT BAYFRONT MARINA</div>
      <div class="marina-copy body-copy">
        <p class="section-head">AT BAYFRONT MARINA YOU GET MORE</p>
        <p>Thank you to every boater who berthed with us this season. Our team is proud to keep the docks safe, clean and welcoming, and we look forward to many more calm mornings and fair winds together in the new year.</p>
        <ul class="tick-list">
          <li><svg width="6" height="6" viewBox="0 0 6 6"><path d="M1 3l1.5 1.5L5 1.5" stroke="#2bb3dc" fill="none" stroke-width="1"/></svg>Protected deep water berths</li>
          <li><svg width="6" height="6" viewBox="0 0 6 6"><path d="M1 3l1.5 1.5L5 1.5" stroke="#2bb3dc" fill="none" stroke-width="1"/></svg>Free wifi on all docks</li>
          <li><svg width="6" height="6" viewBox="0 0 6 6"><path d="M1 3l1.5 1.5L5 1.5" stroke="#2bb3dc" fill="none" stroke-width="1"/></svg>Clean restrooms and showers</li>
          <li><svg width="6" height="6" viewBox="0 0 6 6"><path d="M1 3l1.5 1.5L5 1.5" stroke="#2bb3dc" fill="none" stroke-width="1"/></svg>Full service boatyard</li>
          <li><svg width="6" height="6" viewBox="0 0 6 6"><path d="M1 3l1.5 1.5L5 1.5" stroke="#2bb3dc" fill="none" stroke-width="1"/></svg>Secure gated parking</li>
          <li><svg width="6" height="6" viewBox="0 0 6 6"><path d="M1 3l1.5 1.5L5 1.5" stroke="#2bb3dc" fill="none" stroke-width="1"/></svg>Friendly harbor staff</li>
        </ul>
        <p class="section-head">DIRECTORY OF BAYFRONT MARINA BUSINESSES</p>
        <ul class="tick-list">
          <li><svg width="6" height="6" viewBox="0 0 6 6"><circle cx="3" cy="3" r="1.5" fill="#d7263d"/></svg>Bay Marine Electronics</li>
          <li><svg width="6" height="6" viewBox="0 0 6 6"><circle cx="3" cy="3" r="1.5" fill="#d7263d"/></svg>Harbor Rigging Works</li>
          <li><svg width="6" height="6" viewBox="0 0 6 6"><circle cx="3" cy="3" r="1.5" fill="#d7263d"/></svg>Shoreline Canvas Shop</li>
          <li><svg width="6" height="6" viewBox="0 0 6 6"><circle cx="3" cy="3" r="1.5" fill="#d7263d"/></svg>Dockside Yacht Sales</li>
          <li><svg width="6" height="6" viewBox="0 0 6 6"><circle cx="3" cy="3" r="1.5" fill="#d7263d"/></svg>Keel and Hull Repair</li>
          <li><svg width="6" height="6" viewBox="0 0 6 6"><circle cx="3" cy="3" r="1.5" fill="#d7263d"/></svg>Tidewater Sails</li>
        </ul>
      </div>
      <div class="marina-contact">
        <div class="marina-badge"><i></i>BAYFRONT MARINA</div>
        <div class="body-copy">(510) 555-0148<br>www.bayfrontmarina.example</div>
      </div>
    </article>

    <article class="spread-page spread-right">
      <h2 class="feature-title out-title">THEY ARE ALL OUT THERE SOMEWHERE</h2>
      <p class="out-intro body-copy">Every winter our readers scatter across the globe, chasing trade winds and quiet anchorages. We caught up with a few crews to hear where the season has taken them and what they have learned along the way.</p>
      <div class="sail-photo" role="img" aria-label="Photo of sailboats with white sails on a hazy bay"></div>
      <p class="out-col body-copy">From the Sea of Cortez to the South Pacific, the stories arrive by satellite and sometimes by postcard. Each one reminds us why we first cast off the lines.</p>
      <div class="callout"><b>SEND US YOUR NEWS</b>Share your cruise, photos and tips with the crew for the next issue of the magazine.</div>
      <p class="out-text2 body-copy">Long passages teach patience, and every landfall brings new friends. One couple spent three weeks waiting for a weather window, then crossed in perfect conditions. Another crew rebuilt a broken rudder on a remote beach using only spare parts aboard.</p>
      <div class="photo-row">
        <div class="photo-a" role="img" aria-label="Photo of a yacht at anchor in a calm bay"></div>
        <div class="photo-b" role="img" aria-label="Photo of a beach with palm trees"></div>
        <div class="photo-c" role="img" aria-label="Photo of a tropical coastline"></div>
      </div>
      <div class="ad">
        <div class="ad-mark"></div>
        <div class="ad-info">
          <div class="ad-name">TIDEWATER SAILS</div>
          <div class="ad-line"><svg width="7" height="7" viewBox="0 0 10 10"><path d="M2 1l2 2-1 1.5c.8 1.5 1.8 2.5 3 3L7.5 6l2 2-1.5 1.5C4.5 9 1 5.5.5 2.5z" fill="#0f3f7a"/></svg>(510) 555-0148</div>
          <div class="ad-line"><svg width="7" height="7" viewBox="0 0 10 10"><path d="M5 .5a3.5 3.5 0 0 1 3.5 3.5C8.5 6.5 5 9.5 5 9.5S1.5 6.5 1.5 4A3.5 3.5 0 0 1 5 .5z" fill="#0f3f7a"/><circle cx="5" cy="4" r="1.2" fill="#fff"/></svg>1480 Shoreline Avenue, Bayview</div>
          <div class="ad-line"><svg width="7" height="7" viewBox="0 0 10 10"><circle cx="5" cy="5" r="4" stroke="#0f3f7a" fill="none"/><path d="M1 5h8M5 1c2 2.5 2 5.5 0 8M5 1c-2 2.5-2 5.5 0 8" stroke="#0f3f7a" fill="none" stroke-width=".7"/></svg>www.tidewatersails.example</div>
        </div>
      </div>
    </article>
  </section>

</main>
</body>
</html>
```